Digital Marketing Online Shop Needs a Home Page Web Design

Here is some background on the new home page and the message we want to relay to people visiting our site.
The new site design will be very similar to the following sites
http://plivora.com/
https://quillmarsh.com/
http://barelytidy.io/
http://craftturnip.com/
http://clipmelon.com/
We are a small marketing agency of 3 and we have built up and impressive contact list of partners over the last 16 years to help our customers take their digital marketing to the next level.
The four core areas of products we will be promoting and selling through our online shop are the following :
Web design
Content marketing
Graphic design
Coaching
We operate our agency in a new way, not the old school way so our customers can receive on-demand marketing.
We plan to have an online shop so visitors can purchase some of our services, very similar to how Quill Marshing and Craft Turnip offer their services.
In the end, we want the same call to action layout as Plivora, Quill Marsh and Craft Turnip, however, since we are an agency we would like to blend in Barely Tidy's layout.
We want the customer to either contact us about our services or purchase one of the services from our shop.
We are trying to make the whole digital marketing experience more transactional like retail and not so traditional servicey. :-)
It is from our years of experience and finding the right partners that allows us to offer this type of solution to businesses in the Maritime Provinces (New Brunswick, Nova Scotia, Prince Edward Island, Canada).
Also, because we are offering more of an on-demand/self serve option and we have lower overhead, we hope to pass along great pricing to our customers for their marketing needs. We really want this offer to expand outside of our local market in Saint John, New Brunswick.
I would also like to have a call to action written for a hero image at the top of the page, like the Plivora site.
After that I would like the content to flow through similar to Quill Marsh & Plivora. But mix in some of the agency like content you see with Clipmelon, Barely Tidy.
I have also included the first draft of the content for our home page.
Menu Items will be About, How We Work, Learn, Shop, Contact
Please let me know if you need anything else.
Small businesses, 1-10 person companies with up to 5 million in revenue. Mostly service companies, but some retail.
Marketing
1 page

```html
<!DOCTYPE html>
<html lang="en">
<head>
<meta charset="utf-8">
<title>Tidewell Digital — Home</title>
<link href="https://fonts.googleapis.com/css2?family=Raleway:wght@300;400;500;600;700&family=Open+Sans:wght@400;600;700&display=swap" rel="stylesheet">
<style>
:root{
  --blue:#1e73c8;
  --blue-dark:#175ea6;
  --ink:#333;
  --muted:#666;
  --line:#d9d9d9;
  --band:#ececec;
  --dark:#353535;
  --white:#fff;
  --star:#f2a600;
}
*{box-sizing:border-box;margin:0;padding:0}
html,body{width:1200px;height:3475px;overflow:hidden}
body{position:relative;background:var(--white);font-family:"Open Sans",Arial,sans-serif;color:var(--ink)}
.abs{position:absolute}

/* header */
.site-header{left:0;top:0;width:1200px;height:94px}
.brand{left:134px;top:32px;display:flex;align-items:center;gap:10px}
.brand-square{width:22px;height:22px;background:var(--blue)}
.brand-name{font-family:"Open Sans",sans-serif;font-weight:600;font-size:19px;color:var(--ink);line-height:1}
.main-nav{right:134px;top:36px;display:flex;gap:34px;font-size:14px;font-family:"Open Sans",sans-serif}
.main-nav a{color:var(--ink);text-decoration:none}
.main-nav a.active{color:var(--blue)}

/* hero */
.hero{left:0;top:95px;width:1200px;height:519px;background:linear-gradient(180deg,#d9dde0 0%,#eef0f1 40%,#c9ccce 70%,#8e8e8f 100%)}
.hero-arrow{top:245px;width:22px;height:30px;background:rgba(90,90,90,.5)}
.hero-box{left:401px;top:130px;width:401px;height:257px;background:rgba(255,255,255,.88);text-align:center;padding:30px 22px 0}
.hero-box h1{font-family:"Raleway",sans-serif;font-weight:700;color:var(--blue);font-size:23px;line-height:30px;text-transform:uppercase}
.hero-box p{font-size:14px;line-height:21px;color:var(--ink);margin-top:8px}
.hero-actions{display:flex;justify-content:center;gap:14px;margin-top:22px}
.btn{display:inline-block;background:var(--blue);color:var(--white);font-weight:700;font-size:14px;text-decoration:none;text-transform:uppercase;padding:0 20px;height:44px;line-height:44px}

/* intro */
.intro{left:130px;top:680px;width:940px;text-align:center;font-family:"Raleway",sans-serif;font-weight:300;font-size:31px;line-height:44px;color:var(--ink)}

/* services */
.service{width:459px;height:336px;background:var(--blue);color:var(--white);text-align:center;padding:34px 34px 0}
.service svg{width:40px;height:40px}
.service h2{font-family:"Raleway",sans-serif;font-weight:500;font-size:30px;margin-top:14px}
.service p{font-size:10.5px;line-height:16px;margin-top:12px}
.outline-btn{display:inline-block;border:1px solid currentColor;font-size:10px;text-transform:uppercase;padding:0 14px;height:40px;line-height:38px;margin-top:20px;color:inherit;text-decoration:none}

/* portfolio */
.portfolio{left:0;top:1576px;width:1200px;height:614px;background:var(--dark)}
.tabs{left:0;top:60px;width:1200px;text-align:center;font-family:"Raleway",sans-serif;font-size:15px;color:#999}
.tabs span{margin:0 8px}
.tabs .on{color:var(--white);border-bottom:2px solid var(--white);padding-bottom:6px}
.thumb{height:197px}

/* features */
.feature{width:480px;text-align:center}
.feature svg{width:38px;height:38px}
.feature h3{font-family:"Raleway",sans-serif;font-weight:500;color:var(--blue);font-size:23px;margin-top:6px}
.feature p{font-size:12px;line-height:19px;color:var(--muted);margin-top:8px}
.feature .outline-btn{color:var(--ink);border-color:#999;padding:0 18px;height:42px;line-height:40px}

/* stats */
.stats{left:0;top:2607px;width:1200px;height:127px;background:var(--band)}
.stat{top:40px;width:200px;text-align:center}
.stat b{display:block;font-family:"Raleway",sans-serif;font-weight:700;font-size:30px;color:var(--blue);line-height:34px}
.stat span{font-size:12px;color:var(--blue)}

/* testimonials */
.section-title{left:0;width:1200px;text-align:center;font-family:"Raleway",sans-serif;font-weight:500;font-size:24px;color:var(--blue)}
.quote{width:296px;height:160px;border:1px solid var(--line);background:var(--white);padding:20px 18px 0 20px;font-size:11.5px;line-height:20px;color:var(--muted)}
.quote .mark{position:absolute;left:20px;top:12px;font-family:Georgia,serif;font-size:44px;color:#ccc;line-height:1}
.quote p{text-indent:42px}
.quote::after{content:"";position:absolute;right:40px;bottom:-12px;width:22px;height:22px;background:var(--white);border-right:1px solid var(--line);border-bottom:1px solid var(--line);transform:rotate(45deg)}
.author{text-align:right;font-size:12px;color:var(--ink);width:180px}
.author small{font-size:9px;color:var(--muted)}
.author .stars{display:block;color:var(--star);font-size:10px;letter-spacing:1px}
.avatar{width:36px;height:36px;background:linear-gradient(135deg,#b9a48f,#7d6d60)}
.dots{left:0;top:3098px;width:1200px;text-align:center}
.dots i{display:inline-block;width:8px;height:8px;border-radius:50%;background:#ccc;margin:0 7px}
.dots i.on{background:#333}

/* cta */
.cta{left:0;top:3207px;width:1200px;height:157px;background:var(--band);text-align:center;padding-top:42px}
.cta p{font-size:16px;color:var(--ink)}
.cta .btn{margin-top:12px;height:42px;line-height:42px;padding:0 18px;font-size:15px}

/* footer */
.footer-nav{left:134px;top:3393px;font-size:11px;color:var(--ink)}
.footer-nav span{margin:0 6px;color:#999}
.copyright{left:134px;top:3424px;font-size:10px;color:var(--muted)}
.social{right:134px;top:3395px;display:flex;gap:6px}
.social i{display:block;width:27px;height:27px;border-radius:50%}
</style>
</head>
<body>

<header class="site-header abs">
  <div class="brand abs">
    <span class="brand-square"></span>
    <span class="brand-name">Tidewell Digital</span>
  </div>
  <nav class="main-nav abs">
    <a class="active" href="#">Home</a><a href="#">About</a><a href="#">How We Work</a><a href="#">Learn</a><a href="#">Shop</a><a href="#">Contact</a>
  </nav>
</header>

<section class="hero abs" role="img" aria-label="Photo of a smiling man in a red sweater using a tablet in a bright office by large windows">
  <div class="hero-arrow abs" style="left:0"></div>
  <div class="hero-arrow abs" style="right:0"></div>
  <div class="hero-box abs">
    <h1>Want an online presence<br>for your small business?</h1>
    <p>Give your business the exposure it deserves! Get<br>started by ordering services directly from the shop<br>or by shooting us an email</p>
    <div class="hero-actions"><a class="btn" href="#">Shop</a><a class="btn" href="#">Contact</a></div>
  </div>
</section>

<h2 class="intro abs">We’ll help you move your business into the digital world, so you can get back to doing what you love.</h2>

<article class="service abs" style="left:132px;top:809px">
  <svg viewBox="0 0 40 40" fill="#fff"><path d="M33 4c2 0 3 1 3 3L22 24l-5-5L31 5c.6-.6 1.2-1 2-1z"/><path d="M15 21l5 5c0 6-5 9-12 8 3-2 3-4 3-6 0-4 2-7 4-7z"/></svg>
  <h2>Web Design</h2>
  <p>Let’s be honest. Your website is the face of your business in the modern world. When done well, it can communicate personality, expertise, and high-quality of service. And done poorly? Let’s just say it’ll do more harm than good. From total reconstructive surgery to a simple makeover, we’ll help make sure the face of your business is a welcoming one.</p>
  <a class="outline-btn" href="#">Read more</a>
</article>
<article class="service abs" style="left:607px;top:809px">
  <svg viewBox="0 0 40 40" fill="#fff"><path d="M6 15h8l16-8v26L14 25H6z"/><path d="M10 25h6l3 9h-5z"/><rect x="32" y="17" width="4" height="6"/></svg>
  <h2>Content Marketing</h2>
  <p>Content Marketing is the 21st century what traditional advertising was to the ’60s. Thanks to the power of the internet, so many businesses have never had such access to their customers. And so many businesses have never been so lost on how to use it. Our content marketing services create valuable content your audience pays attention to, giving your business the credibility to turn them into lifelong customers.</p>
  <a class="outline-btn" href="#">Read more</a>
</article>
<article class="service abs" style="left:132px;top:1161px">
  <svg viewBox="0 0 40 40" fill="#fff"><path d="M27 5l8 8-19 19-8-8z"/><path d="M7 26l7 7-9 2z"/></svg>
  <h2>Graphic Design</h2>
  <p>Creating a consistent and eye-catching brand for your business is one of the best ways to draw in customers on the web. And nothing builds a brand like top notch graphic design. From display ads and social graphics to stickers and blog headers, our graphic design service has got you covered. Just let us know what you’re looking for and we’ll find a way to make it come to life.</p>
  <a class="outline-btn" href="#">Read more</a>
</article>
<article class="service abs" style="left:607px;top:1161px">
  <svg viewBox="0 0 40 40" fill="#fff"><rect x="4" y="33" width="32" height="3"/><rect x="8" y="20" width="5" height="12"/><rect x="16" y="12" width="5" height="20"/><rect x="24" y="17" width="5" height="15"/><rect x="31" y="24" width="4" height="8"/></svg>
  <h2>Coaching</h2>
  <p>Taking your small business to the next level can be a tricky process. Marketing jargon, confusing tools, and literally millions of resources can make expanding seem like an impossible task. But luckily, you don’t have to do it alone. Our coaching services help you untangle the mess so you can get the most out of your marketing efforts and create an online presence you’ll be proud of.</p>
  <a class="outline-btn" href="#">Read more</a>
</article>

<section class="portfolio abs">
  <div class="tabs abs"><span class="on">Web design</span>|<span>Content marketing</span>|<span>Graphic design</span>|<span>Coaching</span></div>
  <div class="thumb abs" style="left:132px;top:127px;width:297px;background:linear-gradient(180deg,#bfe3e8,#eef6e8 70%,#f6f6f2)" role="img" aria-label="Website template preview with sky and hot air balloons"></div>
  <div class="thumb abs" style="left:452px;top:127px;width:294px;background:linear-gradient(180deg,#3d4a5e 0 8%,#e4f2f1 8% 60%,#9fd0b6 85%,#f2f2f2)" role="img" aria-label="One-page template preview with flat landscape illustration"></div>
  <div class="thumb abs" style="left:769px;top:127px;width:297px;background:linear-gradient(180deg,#3d4a5e 0 8%,#3fb6c6 8%,#54c2cd 100%)" role="img" aria-label="One-page template preview with hands holding a tablet and app icons"></div>
  <div class="thumb abs" style="left:132px;top:349px;width:297px;background:linear-gradient(180deg,#f4f4f4,#e8e8e8 60%,#c9c9c9)" role="img" aria-label="Template preview of a flat illustrated office desk"></div>
  <div class="thumb abs" style="left:452px;top:349px;width:294px;background:linear-gradient(180deg,#fff 0 28%,#2d5a6b 28%,#6f9a7d 70%,#3d6446)" role="img" aria-label="Template preview with waterfall photograph"></div>
  <div class="thumb abs" style="left:769px;top:349px;width:297px;background:linear-gradient(180deg,#2a4a8c,#5d86c8 50%,#d8e4f2)" role="img" aria-label="Travel template preview with balloons in a blue sky"></div>
</section>

<div class="feature abs" style="left:117px;top:2286px">
  <svg viewBox="0 0 40 40" fill="var(--blue)"><circle cx="15" cy="22" r="9"/><circle cx="15" cy="22" r="3.5" fill="#fff"/><rect x="13" y="10" width="4" height="24"/><rect x="3" y="20" width="24" height="4"/><circle cx="29" cy="11" r="6"/><circle cx="29" cy="11" r="2.2" fill="#fff"/></svg>
  <h3>Tidewell Solutions</h3>
  <p>In a world full of JavaScript and CSS, tweets and emojis, pokes and notifications, modern marketing has never seemed more convoluted. But the truth is, it’s never been more accessible either. And we’re here to help you navigate it.</p>
  <a class="outline-btn" href="#">Read more</a>
</div>
<div class="feature abs" style="left:601px;top:2286px">
  <svg viewBox="0 0 40 40" fill="var(--blue)"><rect x="16" y="5" width="8" height="8"/><rect x="19" y="13" width="2" height="7"/><rect x="7" y="19" width="26" height="2"/><rect x="7" y="19" width="2" height="8"/><rect x="19" y="19" width="2" height="8"/><rect x="31" y="19" width="2" height="8"/><rect x="4" y="27" width="8" height="8"/><rect x="16" y="27" width="8" height="8"/><rect x="28" y="27" width="8" height="8"/></svg>
  <h3>Streamlined Marketing Solutions</h3>
  <p>In a world full of JavaScript and CSS, tweets and emojis, pokes and notifications, modern marketing has never seemed more convoluted. But the truth is, it’s never been more accessible either. And we’re here to help you navigate it.</p>
  <a class="outline-btn" href="#">Read more</a>
</div>

<section class="stats abs">
  <div class="stat abs" style="left:148px"><b>21,000</b><span>Nam consectetur</span></div>
  <div class="stat abs" style="left:382px"><b>82%</b><span>Nam consectetur</span></div>
  <div class="stat abs" style="left:616px"><b>18</b><span>Nam consectetur</span></div>
  <div class="stat abs" style="left:850px"><b>6,12,500</b><span>Nam consectetur</span></div>
</section>

<h2 class="section-title abs" style="top:2812px">Testimonials</h2>

<div class="quote abs" style="left:132px;top:2864px"><span class="mark">“</span><p>Mauris quis sodales enim, semper ultricies massa. Pellentesque risus dolor, tristique vel facilisis at, laoreet ut elit. Fusce id augue at metus cursus pulvinar. In nec lectus porttitor, porttitor velit vel, tempus tortor.</p></div>
<div class="quote abs" style="left:452px;top:2864px"><span class="mark">“</span><p>Mauris quis sodales enim, semper ultricies massa. Pellentesque risus dolor, tristique vel facilisis at, laoreet ut elit. Fusce id augue at metus cursus pulvinar. In nec lectus porttitor, porttitor velit vel, tempus tortor.</p></div>
<div class="quote abs" style="left:770px;top:2864px"><span class="mark">“</span><p>Mauris quis sodales enim, semper ultricies massa. Pellentesque risus dolor, tristique vel facilisis at, laoreet ut elit. Fusce id augue at metus cursus pulvinar. In nec lectus porttitor, porttitor velit vel, tempus tortor.</p></div>

<div class="author abs" style="left:160px;top:3036px">Mark Ellis, <small>City name</small><span class="stars">★★★★★</span></div>
<div class="avatar abs" style="left:346px;top:3034px" role="img" aria-label="Customer portrait"></div>
<div class="author abs" style="left:480px;top:3036px">Mark Ellis, <small>City name</small><span class="stars">★★★★★</span></div>
<div class="avatar abs" style="left:666px;top:3034px" role="img" aria-label="Customer portrait"></div>
<div class="author abs" style="left:798px;top:3036px">Mark Ellis, <small>City name</small><span class="stars">★★★★★</span></div>
<div class="avatar abs" style="left:984px;top:3034px" role="img" aria-label="Customer portrait"></div>

<div class="dots abs"><i class="on"></i><i></i><i></i><i></i></div>

<section class="cta abs">
  <p>Sed ultricies ipsum ut justo pellentesque, id scelerisque tellus ullamcorper</p>
  <a class="btn" href="#">Get started</a>
</section>

<nav class="footer-nav abs">Home<span>|</span>About<span>|</span>How We Work<span>|</span>Learn<span>|</span>Shop<span>|</span>Contact</nav>
<p class="copyright abs">Copyright © 2016 Company name. All rights reserved.</p>
<div class="social abs">
  <i style="background:#3b5998"></i><i style="background:#1da1f2"></i><i style="background:#0077b5"></i><i style="background:#dd4b39"></i><i style="background:#cb2027"></i><i style="background:#e52d27"></i>
</div>

</body>
</html>
```